Spiral Bound Classy Marketing Planner Cover Design

A5 marketing planner book cover requiredClassy, minimalist design for female entrepreneurs. The inside is all in grey and is a minimalist uncluttered design. Name of the planner is It's Time Marketing Recipe PlannerHeader font inside the planner is Shelby and other font is Lato Brand colours are teal and grey.The printing format has changed and as such I am looking for a new cover design to make this marketing planner look classy and engaging. Would prefer my logo to be on the back. We have the option for a 10cm x 10cm foil detail to be added on the front cover, feel free to add this to your design.This is for a spiral bound book - A5 front cover and A5 back cover - no spine required.

Target Market(s)

Female entrepreneurs

Industry/Entity Type

Marketing

Colors
33b8a4
ffffff

Requirements
Must have
• Front and back designs
• A5
Should not have
• Large illustrations
• People in the design
• Spine design

```html
<!DOCTYPE html>
<html lang="en">
<head>
<meta charset="utf-8">
<title>Bold Hour Promo Blueprint Planner – Front Cover</title>
<link rel="stylesheet" href="https://fonts.googleapis.com/css2?family=Dancing+Script:wght@500&family=Lato:wght@400&display=swap">
<style>
  :root {
    --page-bg: #ffffff;
    --mint: #5be2a6;
    --panel: #ffffff;
    --ink-dark: #141515;
    --ink-mid: #3c3f3f;
    --ink-light: #cfd4d2;
    --ink-pale: #eef0ef;
  }
  * { margin: 0; padding: 0; box-sizing: border-box; }
  html, body {
    width: 1200px;
    height: 1200px;
    overflow: hidden;
    background: var(--page-bg);
  }
  .cover {
    position: absolute;
    left: 242px;
    top: 92px;
    width: 717px;
    height: 1015px;
    overflow: hidden;
  }
  .cover__marble {
    position: absolute;
    inset: 0;
    background:
      radial-gradient(ellipse 60% 35% at 70% 30%, rgba(200,204,202,0.35), transparent 70%),
      radial-gradient(ellipse 45% 30% at 15% 55%, rgba(170,175,173,0.35), transparent 70%),
      linear-gradient(180deg, var(--ink-dark) 0%, #222424 30%, var(--ink-mid) 55%, #a9aeac 78%, var(--ink-light) 90%, var(--ink-pale) 100%);
  }
  .title-frame {
    position: absolute;
    left: 150px;
    top: 274px;
    width: 414px;
    height: 466px;
    border: 10px solid var(--mint);
  }
  .title-panel {
    position: absolute;
    left: 178px;
    top: 305px;
    width: 360px;
    height: 405px;
    background: var(--panel);
    text-align: center;
    color: var(--mint);
  }
  .title-panel__script {
    position: absolute;
    left: 0;
    right: 0;
    top: 30px;
    font-family: "Dancing Script", cursive;
    font-weight: 500;
    font-size: 84px;
    line-height: 1.2;
  }
  .title-panel__rule {
    position: absolute;
    left: 46px;
    width: 268px;
    top: 169px;
    height: 2px;
    background: var(--mint);
  }
  .title-panel__name {
    position: absolute;
    left: 0;
    right: 0;
    top: 213px;
    font-family: "Lato", sans-serif;
    font-weight: 400;
    font-size: 38px;
    line-height: 48px;
    letter-spacing: 0.5px;
    text-transform: uppercase;
  }
</style>
</head>
<body>
  <main class="cover">
    <div class="cover__marble" role="img" aria-label="Black, grey and white fluid marble ink texture filling the cover"></div>
    <div class="title-frame"></div>
    <section class="title-panel">
      <h1 class="title-panel__script">Bold Hour</h1>
      <div class="title-panel__rule"></div>
      <p class="title-panel__name">Promo<br>Blueprint<br>Planner</p>
    </section>
  </main>
</body>
</html>
```